ORVALO Global Commerce Inc.
Kareem Bin-Sahwan
Vice President
Unit 385, 2096 Pellmore Crescent Toronto, Ontario, Canada M4R 2K6
kareem@orvaloglobal.ca
www.orvaloglobal.ca
The company's name is "ORVALO Global Commerce Inc." The company's new logo is only stating ORVALO, i need the wording "Global Commerce Inc." to be added next to the logo at different designs for me to choose from.
The logo of the company with the wording "Global Commerce Inc." at different backgrounds and design for me to choose from.

```html
<!DOCTYPE html>
<html lang="en">
<head>
<meta charset="utf-8">
<title>ORVALO Global Commerce Inc. – Business Card</title>
<link rel="stylesheet" href="https://fonts.googleapis.com/css2?family=Exo+2:wght@400;500&display=swap">
<style>
  :root {
    --backdrop: #2b2c2e;
    --card: #ffffff;
    --ink: #3d3f43;
    --ink-soft: #55585d;
    --accent: #2e86c8;
    --icon-grey: #6d7075;
  }
  * { margin: 0; padding: 0; box-sizing: border-box; }
  html, body {
    width: 1200px; height: 816px; overflow: hidden;
    background: var(--backdrop);
    font-family: "Exo 2", sans-serif;
  }
  .card {
    position: absolute; left: 75px; top: 108px;
    width: 1050px; height: 600px;
    background: var(--card);
    border-radius: 42px;
    color: var(--ink);
  }
  .identity {
    position: absolute; left: 60px; top: 132px;
    display: flex; align-items: center; gap: 20px;
  }
  .identity__name {
    font-size: 26px; font-weight: 500; letter-spacing: 1.5px; line-height: 1.15;
  }
  .identity__role {
    font-size: 21px; letter-spacing: 2px; color: var(--ink-soft); line-height: 1.2;
  }
  .rule {
    position: absolute; left: 0; top: 212px;
    width: 470px; height: 4px; background: var(--accent);
  }
  .icon { width: 46px; height: 46px; flex: none; }
  .contacts {
    position: absolute; left: 60px; top: 258px;
    list-style: none; display: flex; flex-direction: column; gap: 30px;
  }
  .contact { display: flex; align-items: center; gap: 22px; }
  .contact__text { font-size: 20px; line-height: 1.3; letter-spacing: 0.5px; color: var(--ink-soft); }
  .brand {
    position: absolute; left: 580px; top: 238px;
  }
  .brand__row { display: flex; align-items: center; gap: 18px; }
  .brand__mark { width: 30px; height: 30px; background: var(--accent); flex: none; }
  .brand__name {
    font-size: 92px; font-weight: 500; letter-spacing: 4px; color: var(--ink); line-height: 1;
  }
  .brand__tagline {
    margin: 14px 0 0 48px;
    font-size: 27px; font-weight: 400; letter-spacing: 3.5px; color: var(--ink-soft);
  }
</style>
</head>
<body>
  <div class="card">
    <div class="identity">
      <svg class="icon" viewBox="0 0 46 46" aria-hidden="true">
        <circle cx="23" cy="23" r="23" fill="var(--icon-grey)"/>
        <circle cx="23" cy="18" r="7" fill="#fff"/>
        <path d="M11 35c2-7 7-10 12-10s10 3 12 10z" fill="#fff"/>
      </svg>
      <div>
        <div class="identity__name">KAREEM BIN-SAHWAN</div>
        <div class="identity__role">Vice President</div>
      </div>
    </div>
    <div class="rule"></div>

    <ul class="contacts">
      <li class="contact">
        <svg class="icon" viewBox="0 0 46 46" aria-hidden="true">
          <circle cx="23" cy="23" r="23" fill="var(--accent)"/>
          <rect x="16" y="11" width="14" height="24" rx="2.5" fill="none" stroke="#fff" stroke-width="2.5"/>
          <circle cx="23" cy="31" r="1.5" fill="#fff"/>
        </svg>
        <div class="contact__text">012 555 0148<br>012 555 0149</div>
      </li>
      <li class="contact">
        <svg class="icon" viewBox="0 0 46 46" aria-hidden="true">
          <circle cx="23" cy="23" r="23" fill="var(--accent)"/>
          <rect x="12" y="13" width="22" height="15" rx="1.5" fill="none" stroke="#fff" stroke-width="2.5"/>
          <path d="M18 34h10M23 28v6" stroke="#fff" stroke-width="2.5"/>
        </svg>
        <div class="contact__text">kareem@orvaloglobal.ca<br>www.orvaloglobal.ca</div>
      </li>
      <li class="contact">
        <svg class="icon" viewBox="0 0 46 46" aria-hidden="true">
          <circle cx="23" cy="23" r="23" fill="var(--accent)"/>
          <path d="M23 36s-8-9-8-15a8 8 0 0 1 16 0c0 6-8 15-8 15z" fill="#fff"/>
          <circle cx="23" cy="21" r="3" fill="var(--accent)"/>
        </svg>
        <div class="contact__text">Unit 385, 2096 Pellmore Crescent<br>Toronto, ON M4R 2K6</div>
      </li>
    </ul>

    <div class="brand">
      <div class="brand__row">
        <div class="brand__mark"></div>
        <div class="brand__name">ORVALO</div>
      </div>
      <div class="brand__tagline">Global Commerce Inc.</div>
    </div>
  </div>
</body>
</html>
```